Brimvale Website

I need a design of homepage for a health and wellness center. We considers self to be young and fresh and want something along that design. We want a main picture/logo/design (or all three), and underneath that 4 pictures to depict what services we do. The four services are Orthopedic Rehab, Neurological Rehab, Speech Pathology and Float. I have attached our logo, and some pictures that might be helpful, but the pictures don't have to be included. Here is an example of what I would like it look. http://pixelbazaar.net/web-design/contests/lumotrek-website-design-needed-more-work-come-submit-517306/entries/84126759

```html
<!DOCTYPE html>
<html lang="en">
<head>
<meta charset="utf-8">
<title>Brimvale Centre for Health + Wellness</title>
<link href="https://fonts.googleapis.com/css2?family=Open+Sans:ital,wght@0,400;0,600;0,700;1,400;1,600&display=swap" rel="stylesheet">
<style>
:root{
  --teal:#7fb3a5;
  --teal-dark:#4f9a86;
  --green:#9dbb16;
  --green-dark:#86a30e;
  --ink:#1f2229;
  --text:#3c3c3c;
  --muted:#6b6b6b;
  --sky:#cdeef6;
  --page:#f6f6f7;
  --line:#d7d9dc;
  --white:#ffffff;
}
*{box-sizing:border-box;margin:0;padding:0}
html,body{width:788px;height:1200px;overflow:hidden}
body{font-family:"Open Sans",Arial,sans-serif;color:var(--text);background:var(--page);position:relative}
a{color:inherit;text-decoration:none}

.topbar{position:absolute;left:0;top:0;width:788px;height:16px;background:var(--teal);color:var(--white);font-size:8.5px;font-weight:600}
.topbar .links{position:absolute;left:122px;top:2px}
.topbar .account{position:absolute;right:114px;top:2px;display:flex;align-items:center;gap:6px}
.topbar .dot{width:8px;height:8px;border-radius:50%;background:var(--white);opacity:.85}

.header{position:absolute;left:0;top:16px;width:788px;height:56px;background:var(--white);border-bottom:1px solid #e3e6e6}
.brand{position:absolute;left:122px;top:12px;display:flex;align-items:center;gap:8px}
.brand .mark{width:28px;height:28px;border-radius:50%;background:var(--teal)}
.brand .name{font-size:26px;font-weight:400;color:var(--teal-dark);letter-spacing:.5px}
.phone{position:absolute;right:116px;top:12px;display:flex;align-items:center;gap:4px;font-size:15px;color:#2d2d2d}
.nav{position:absolute;right:116px;top:34px;display:flex;gap:15px;font-size:9.5px;font-weight:600;color:var(--teal-dark)}
.nav .current{color:var(--ink)}

.hero{position:absolute;left:0;top:72px;width:788px;height:268px;background:radial-gradient(circle at 570px 150px,#ffffff 0,#e8f8fb 90px,var(--sky) 220px)}
.hero-band{position:absolute;left:0;top:340px;width:788px;height:6px;background:var(--green)}
.hero h1{position:absolute;left:128px;top:70px;font-size:29px;line-height:36px;font-weight:600;color:var(--ink)}
.hero h1 span{color:var(--white)}
.hero p{position:absolute;left:127px;top:156px;width:330px;font-size:10.5px;line-height:15px;color:#2a2a2a}
.hero .emblem{position:absolute;left:470px;top:30px;width:210px;height:210px;border-radius:50%;background:radial-gradient(circle,#ffffff 0,rgba(255,255,255,.6) 55%,rgba(255,255,255,0) 72%)}
.hero .arrow{position:absolute;top:108px}

.section-title{position:absolute;left:118px;width:552px;display:flex;align-items:center;gap:8px;font-size:12px;color:var(--teal-dark);font-weight:400}
.section-title .rule{flex:1;height:1px;background:var(--line)}
.section-title .bullet{width:11px;height:11px;border-radius:50%;background:var(--teal);border:2px solid #c9dc7a}

.services{position:absolute;left:118px;top:382px;width:560px;height:200px}
.card{position:absolute;top:0;width:120px}
.card .photo{height:82px;border-bottom:3px solid var(--teal)}
.card h3{margin-top:6px;text-align:center;font-size:10px;font-weight:600;color:var(--ink);letter-spacing:.1px}
.card h3 span{color:var(--green)}
.card .body{margin-top:2px;height:94px;border:1px solid #d5d6d8;border-top:none;border-radius:0 0 4px 4px;background:#f3f3f4;box-shadow:0 2px 0 #e0e0e2;padding:2px 4px;font-size:7px;line-height:13.6px;text-align:center;color:var(--muted)}
.card .tab{position:absolute;right:-12px;top:159px;width:12px;height:22px;background:var(--green);border-radius:0 3px 3px 0}

.divider{position:absolute;left:0;top:602px;width:788px;height:1px;background:var(--line)}

.welcome{position:absolute;left:122px;top:617px;width:546px;text-align:center}
.welcome h2{font-size:12.5px;font-weight:600;color:var(--teal-dark)}
.welcome p{font-size:8.3px;line-height:13.4px;color:#444;margin-top:2px}
.welcome .first{margin-top:5px}
.btn-read{display:inline-block;margin-top:9px;width:64px;height:21px;line-height:21px;border-radius:6px;background:var(--green);box-shadow:0 2px 0 var(--green-dark);color:var(--white);font-size:7.5px;font-weight:700}

.testimonial{position:absolute;left:0;top:770px;width:788px;height:242px;background:#f3f4f6}
.avatar{position:absolute;left:356px;top:44px;width:76px;height:76px;border-radius:50%;background:linear-gradient(160deg,#f2e4d8,#c99d78);border:5px solid var(--white);box-shadow:0 1px 4px rgba(0,0,0,.2)}
.quote{position:absolute;left:130px;top:150px;width:528px;text-align:center;font-size:7.6px;line-height:14.5px;font-style:italic;color:#555}
.author{position:absolute;left:0;top:188px;width:788px;text-align:center;font-size:8.5px;font-style:italic;font-weight:600;color:var(--ink)}
.pager{position:absolute;left:379px;top:220px;display:flex;gap:3px}
.pager i{width:5px;height:5px;border-radius:50%;background:var(--teal)}
.pager i:first-child{background:#4e6a63}

.contact{position:absolute;left:0;top:1012px;width:788px;height:106px;background:#f7f7f8;border-top:1px solid #e2e3e5}
.contact h2{position:absolute;left:0;top:8px;width:780px;text-align:center;font-size:12px;font-weight:600;color:var(--teal-dark)}
.field{position:absolute;font-size:8.5px;color:#333;display:flex;align-items:center;gap:8px}
.field .box{height:18px;background:var(--white);border:1px solid #c9cacc}
.submit{position:absolute;left:570px;top:41px;width:97px;height:34px;border-radius:17px;background:linear-gradient(#b6d034,var(--green));box-shadow:0 2px 0 var(--green-dark);color:var(--white);font-size:11px;font-weight:700}
.submit .ring{position:absolute;left:2px;top:2px;width:30px;height:30px;border-radius:50%;background:var(--white);border:2px solid var(--green-dark)}
.submit .label{position:absolute;left:41px;top:9px}

.footer{position:absolute;left:0;top:1118px;width:788px;height:82px;background:var(--green);border-top:2px solid var(--green-dark)}
.social{position:absolute;left:352px;top:11px;display:flex;gap:3px}
.social i{width:19px;height:19px;border-radius:50%;background:#2f6d9e;border:1px solid var(--white)}
.social i:last-child{background:#3a3a3a}
.footer-nav{position:absolute;left:0;top:40px;width:788px;display:flex;justify-content:center;gap:23px;font-size:7.5px;font-weight:600;color:var(--white)}
.copyright{position:absolute;left:0;top:62px;width:788px;height:20px;background:var(--green-dark);text-align:center;font-size:7px;line-height:18px;color:#eef3d6}
</style>
</head>
<body>

<div class="topbar">
  <div class="links">CONTACT &nbsp;| ASK A QUESTION | PHOTOGALLERY | PRESS</div>
  <div class="account"><span class="dot"></span><span class="dot"></span>&nbsp;SIGN IN &nbsp;| &nbsp;REGISTER</div>
</div>

<header class="header">
  <div class="brand"><span class="mark"></span><span class="name">Brimvale</span></div>
  <div class="phone">
    <svg width="16" height="16" viewBox="0 0 16 16"><circle cx="8" cy="8" r="7" fill="none" stroke="#9dbb16" stroke-width="1.4"/><path d="M5.5 4.5l1.5 0 .6 1.8-.9.7c.4 1 1.1 1.8 2.2 2.3l.7-.9 1.8.6v1.5c-3.6.2-6.1-2.5-5.9-6z" fill="#9dbb16"/></svg>
    014 628 3907
  </div>
  <nav class="nav"><a class="current">HOME</a><a>ABOUT US</a><a>SERVICES</a><a>TESTIMONIALS</a><a>CONTACT US</a></nav>
</header>

<section class="hero">
  <h1>We can help you <span>recover<br>and perform better</span></h1>
  <p>Lorem ipsum dolor sit amet, consectetuer adipiscing elit, sed diam nonummy nibh euismod tincidunt ut laoreet dolore magna ali quam er at volut pat. Ut wisi enim ad minim veniam.</p>
  <div class="emblem" role="img" aria-label="Soft glowing emblem area"></div>
  <svg class="arrow" style="left:90px" width="30" height="30" viewBox="0 0 30 30"><circle cx="15" cy="15" r="13" fill="none" stroke="#555" stroke-width="2.4"/><path d="M17 9l-6 6 6 6" fill="none" stroke="#555" stroke-width="2.4"/></svg>
  <svg class="arrow" style="left:668px" width="30" height="30" viewBox="0 0 30 30"><circle cx="15" cy="15" r="13" fill="none" stroke="#555" stroke-width="2.4"/><path d="M13 9l6 6-6 6" fill="none" stroke="#555" stroke-width="2.4"/></svg>
</section>
<div class="hero-band"></div>

<div class="section-title" style="top:361px"><span class="bullet"></span><span class="rule"></span>We are a Health and Wellness Centre<span class="rule"></span><span class="bullet"></span></div>

<section class="services">
  <article class="card" style="left:0">
    <div class="photo" role="img" aria-label="Therapist treating a patient's knee in a brace" style="background:linear-gradient(135deg,#9fb6c9,#3a3a3a)"></div>
    <h3>ORTHOPEDIC <span>REHAB</span></h3>
    <div class="body">Lorem ipsum dolor sit amet, consectetuer adipiscing elit, sed diam nonummy nibh euismod tincidunt ut laoreet dolore magna aliquam erat volutpat. Ut wisi enim ad minim veniam.</div>
    <span class="tab"></span>
  </article>
  <article class="card" style="left:139px">
    <div class="photo" role="img" aria-label="Glowing blue neuron network" style="background:radial-gradient(circle at 60% 45%,#6fa8ff,#1b3a8c 60%,#0b1230)"></div>
    <h3>NEUROLOGICAL <span>REHAB</span></h3>
    <div class="body">Lorem ipsum dolor sit amet, consectetuer adipiscing elit, sed diam nonummy nibh euismod tincidunt ut laoreet dolore magna aliquam erat volutpat. Ut wisi enim ad minim veniam.</div>
    <span class="tab"></span>
  </article>
  <article class="card" style="left:280px">
    <div class="photo" role="img" aria-label="Therapist playing with a young child" style="background:linear-gradient(135deg,#cdbfae,#7a5a4a 60%,#c24a7a)"></div>
    <h3>SPEECH <span>PATHOLOGY</span></h3>
    <div class="body">Lorem ipsum dolor sit amet, consectetuer adipiscing elit, sed diam nonummy nibh euismod tincidunt ut laoreet dolore magna aliquam erat volutpat. Ut wisi enim ad minim veniam.</div>
    <span class="tab"></span>
  </article>
  <article class="card" style="left:422px">
    <div class="photo" role="img" aria-label="Float therapy pod lit in blue" style="background:linear-gradient(160deg,#e9e5df,#c9c3ba 60%,#6fb7e0)"></div>
    <h3>FLOAT <span>THERAPY</span></h3>
    <div class="body">Lorem ipsum dolor sit amet, consectetuer adipiscing elit, sed diam nonummy nibh euismod tincidunt ut laoreet dolore magna aliquam erat volutpat. Ut wisi enim ad minim veniam.</div>
    <span class="tab"></span>
  </article>
</section>

<div class="divider"></div>

<section class="welcome">
  <h2>Welcome to Brimvale Centre for Health &amp; Wellness</h2>
  <p class="first">Lorem ipsum dolor sit amet, consectetuer adipiscing elit, sed diam nonummy nibh euismod tincidunt ut laoreet dolore magna aliquam erat volutpat. Ut wisi enim ad minim veniam. Lorem ipsum dolor sit amet, consectetur adipisicing elit, sed do eiusmod tempor incididunt ut labore et dolore magna aliqua. Ut enim ad minim veniam, quis nostrud exercitation ullamco laboris nisi ut aliquip ex ea commodo consequat. Duis aute irure dolor in reprehenderit in voluptate velit esse cillum dolore eu fugiat nulla pariatur.</p>
  <p>&nbsp;&nbsp;Ut enim ad minim veniam, quis nostrud exercitation ullamco laboris nisi ut aliquip ex ea commodo consequat. Duis aute irure dolor in reprehenderit in voluptate velit esse cillum dolore eu fugiat nulla pariatur. Excepteur sint occaecat cupidatat non proident, sunt in culpa qui officia deserunt mollit anim id est laborum.</p>
  <a class="btn-read">READ MORE</a>
</section>

<section class="testimonial">
  <div class="section-title" style="top:25px"><span class="bullet"></span><span class="rule"></span>What Clients Think About Us<span class="rule"></span><span class="bullet"></span></div>
  <div class="avatar" role="img" aria-label="Portrait of a smiling client"></div>
  <p class="quote">" &nbsp;Lorem ipsum dolor sit amet, consectetuer adipiscing elit, sed diam nonummy nibh euismod tincidunt ut laoreet dolore magna aliquam erat volutpat. Ut wisi enim ad minim veniam, quis nostrud exerci tation ullam corper. "</p>
  <p class="author">Marla Fenwick</p>
  <div class="pager"><i></i><i></i><i></i></div>
</section>

<section class="contact">
  <h2>Quick Contact</h2>
  <label class="field" style="left:118px;top:42px">Name <span class="box" style="width:111px"></span></label>
  <label class="field" style="left:270px;top:42px">Phone <span class="box" style="width:111px"></span></label>
  <label class="field" style="left:421px;top:42px">E-mail <span class="box" style="width:111px"></span></label>
  <label class="field" style="left:118px;top:73px">Message <span class="box" style="width:400px;height:25px"></span></label>
  <a class="submit"><span class="ring"><svg width="26" height="26" viewBox="0 0 26 26"><path d="M7 19c0-5 3-8 9-8v-3l5 5-5 5v-3c-4 0-7 1-9 4z" fill="#4f9a86"/></svg></span><span class="label">SUBMIT</span></a>
</section>

<footer class="footer">
  <div class="social"><i></i><i></i><i></i><i></i></div>
  <nav class="footer-nav"><a>HOME</a><a>ABOUT US</a><a>SERVICES</a><a>TESTIMONIALS</a><a>CONTACT US</a></nav>
  <div class="copyright">Copyright . 2014. &nbsp;BrimvaleWellnessCentre. All Right Reserved.</div>
</footer>

</body>
</html>
```